Business card for femtech company

Nothing too elaborate but elegant and geared towards the mother and baby market. Prefer full-bleed with logo (attached) rear.

```html
<!DOCTYPE html>
<html lang="en">
<head>
<meta charset="utf-8">
<title>Lunelle — Business Card</title>
<link href="https://fonts.googleapis.com/css2?family=Nunito+Sans:wght@400;600;700&display=swap" rel="stylesheet">
<style>
  :root {
    --bg: #e3e4e6;
    --card: #ffffff;
    --teal: #5cc4b8;
    --teal-faint: #eef8f6;
    --grey: #9b9b9b;
    --ink: #3a3a3a;
    --rule: #d2d2d2;
  }
  * { box-sizing: border-box; margin: 0; padding: 0; }
  html, body { width: 1200px; height: 800px; overflow: hidden; }
  body {
    background: var(--bg);
    font-family: "Nunito Sans", sans-serif;
    position: relative;
  }
  .card {
    position: absolute;
    top: 250px;
    width: 525px;
    height: 300px;
    background: var(--card);
    overflow: hidden;
    box-shadow: 0 2px 6px rgba(0,0,0,0.08);
  }
  .card--back { left: 50px; }
  .card--front { left: 625px; }

  .faint-mark {
    position: absolute;
    border-radius: 50%;
    background: var(--teal-faint);
  }
  .card--back .faint-mark { width: 200px; height: 200px; right: -30px; bottom: -60px; }
  .card--front .faint-mark { width: 190px; height: 190px; right: -30px; bottom: -70px; }

  .wordmark {
    color: var(--grey);
    font-weight: 600;
    letter-spacing: 0.5px;
    line-height: 1;
  }
  .card--back .wordmark {
    position: absolute;
    left: 60px;
    top: 90px;
    font-size: 92px;
  }

  .brand {
    position: absolute;
    right: 30px;
    top: 50px;
    display: flex;
    flex-direction: column;
    align-items: flex-end;
    gap: 14px;
  }
  .brand__dot {
    width: 62px;
    height: 62px;
    border-radius: 50%;
    background: var(--teal);
    margin-right: 70px;
  }
  .brand .wordmark { font-size: 48px; }

  .contact {
    position: absolute;
    left: 26px;
    top: 58px;
    width: 260px;
    color: var(--ink);
  }
  .contact__name {
    color: var(--teal);
    font-weight: 700;
    font-size: 17px;
    letter-spacing: 1px;
    text-transform: uppercase;
  }
  .contact__role { font-size: 13px; margin-top: 1px; }
  .contact__list {
    list-style: none;
    margin-top: 16px;
    font-size: 14px;
    line-height: 1.55;
  }
  .contact__list li { display: flex; align-items: center; gap: 7px; }
  .contact__list svg { width: 12px; height: 12px; flex: none; }
  .contact__rule {
    position: absolute;
    left: 0;
    top: 152px;
    width: 280px;
    height: 1px;
    background: var(--rule);
  }
  .address {
    position: absolute;
    left: 170px;
    top: 166px;
    padding-left: 12px;
    border-left: 1px solid var(--teal);
    font-size: 14px;
    line-height: 1.35;
    color: var(--ink);
  }
</style>
</head>
<body>

  <section class="card card--back" aria-label="Card back">
    <div class="faint-mark" aria-hidden="true"></div>
    <div class="wordmark">lunelle</div>
  </section>

  <section class="card card--front" aria-label="Card front">
    <div class="faint-mark" aria-hidden="true"></div>

    <div class="brand">
      <span class="brand__dot" aria-hidden="true"></span>
      <span class="wordmark">lunelle</span>
    </div>

    <div class="contact">
      <div class="contact__name">Clara Beaumont</div>
      <div class="contact__role">Director</div>
      <ul class="contact__list">
        <li>
          <svg viewBox="0 0 12 12" aria-hidden="true"><path d="M3 1 L5 3.5 L4 5 Q5 7 7 8 L8.5 7 L11 9 L9.5 11 Q5 11 2.5 8 Q1 5.5 1 2.5 Z" fill="var(--teal)"/></svg>
          300-415-2760
        </li>
        <li>
          <svg viewBox="0 0 12 12" aria-hidden="true"><rect x="1" y="2.5" width="10" height="7" fill="none" stroke="var(--teal)" stroke-width="1.2"/><path d="M1 2.5 L6 6.5 L11 2.5" fill="none" stroke="var(--teal)" stroke-width="1.2"/></svg>
          hello@Lunelle.com
        </li>
        <li>
          <svg viewBox="0 0 12 12" aria-hidden="true"><circle cx="6" cy="6" r="5" fill="none" stroke="var(--teal)" stroke-width="1"/><ellipse cx="6" cy="6" rx="2.2" ry="5" fill="none" stroke="var(--teal)" stroke-width="1"/><path d="M1 6 H11" stroke="var(--teal)" stroke-width="1"/></svg>
          www.Lunelle.com
        </li>
      </ul>
      <div class="contact__rule" aria-hidden="true"></div>
      <div class="address">00 dummy city<br>place 0000</div>
    </div>
  </section>

</body>
</html>
```